Facebook Ads for Leading Telemedicine Provider

Need a variation of this advertisement.

Would like to leave everything the same with white as the dominant color but test the pink circle with a different design style

Target Market(s)

Male / Female from 18-65

Industry/Entity Type

Health

Requirements
Must have
• Use the image attached and test a different background

```html
<!DOCTYPE html>
<html lang="en">
<head>
<meta charset="utf-8">
<title>Wello – Free Covid Testing at Home</title>
<link rel="stylesheet" href="https://fonts.googleapis.com/css2?family=Open+Sans:wght@700;800&family=Montserrat:wght@700&display=swap">
<style>
  :root {
    --stage: #1b1b1b;
    --card: #ffffff;
    --lime: #cde32a;
    --teal: #4aa98a;
    --ocean: #0f6fb8;
    --navy: #0b1766;
    --white: #ffffff;
    --sand: #f6ead0;
    --ochre: #e2c27a;
  }
  * { box-sizing: border-box; margin: 0; padding: 0; }
  html, body {
    width: 1200px;
    height: 1000px;
    overflow: hidden;
    background: var(--stage);
  }
  .ad {
    position: absolute;
    left: 337px;
    top: 237px;
    width: 526px;
    height: 526px;
    background: var(--card);
    overflow: hidden;
    font-family: "Open Sans", Arial, sans-serif;
  }
  .ad__circle {
    position: absolute;
    left: -85px;
    top: -15px;
    width: 456px;
    height: 456px;
    border-radius: 50%;
    background: linear-gradient(140deg, var(--lime) 10%, var(--teal) 50%, var(--ocean) 90%);
  }
  .ad__brand {
    position: absolute;
    left: 47px;
    top: 46px;
    font-weight: 800;
    font-size: 32px;
    line-height: 1;
    color: var(--white);
    letter-spacing: -0.5px;
  }
  .ad__headline {
    position: absolute;
    left: 37px;
    top: 142px;
    font-weight: 800;
    font-size: 55px;
    line-height: 59px;
    color: var(--white);
    letter-spacing: 0.2px;
  }
  .ad__cta {
    position: absolute;
    left: 37px;
    top: 355px;
    width: 170px;
    height: 43px;
    border-radius: 6px;
    background: var(--navy);
    color: var(--white);
    font-family: "Montserrat", Arial, sans-serif;
    font-weight: 700;
    font-size: 16px;
    letter-spacing: 1px;
    display: flex;
    align-items: center;
    justify-content: center;
  }
  .ad__url {
    position: absolute;
    left: 34px;
    top: 478px;
    font-family: "Montserrat", Arial, sans-serif;
    font-weight: 700;
    font-size: 11px;
    color: var(--navy);
  }
  .ad__illustration {
    position: absolute;
    left: 236px;
    top: 264px;
    width: 238px;
    height: 240px;
    border-radius: 20px;
    background: linear-gradient(160deg, var(--sand) 0%, var(--ochre) 100%);
  }
  .ad__illustration-badge {
    position: absolute;
    left: 402px;
    top: 205px;
    width: 52px;
    height: 52px;
    border-radius: 50%;
    background: var(--sand);
  }
</style>
</head>
<body>
  <div class="ad">
    <div class="ad__circle"></div>
    <div class="ad__brand">Wello</div>
    <h1 class="ad__headline">Free Covid<br>Testing at<br>Home</h1>
    <div class="ad__cta">BOOK NOW</div>
    <div class="ad__illustration-badge" role="img" aria-label="Virus-free icon"></div>
    <div class="ad__illustration" role="img" aria-label="Illustration of a masked tester with a clipboard greeting a woman at her front door, with a potted plant and welcome mat"></div>
    <div class="ad__url">https://wello.org/covid-testing</div>
  </div>
</body>
</html>
```